Portfolio required for virtual assistant seeking new clients

I require an editable Word template that can be sent to clients. This is a new business venture I am undertaking - working as a virtual assistant (administration work). I will need to find my own clients so would like Wow factor. Target group will be small businesses/legal industry so needs to look professional.
The portfolio will need to note information about me, why hire me, my skill set and credentials. May add testimonials too. I have attached a draft of the amount of text required - still working on this.
I will upload my logo and business card design. I do like consistency.
Colours used Pantone 2745 C and 272 C. Open to other colours but would like to see the main colours of logo incorporated. Images welcome. May insert an image of myself at some stage so please allow for a spot for this photo.
The portfolio will need to be converted to pdf to send by email as well as printable.
Updates

Automatically set for 24 hours apologies did not see this. Now amended

```html
<!DOCTYPE html>
<html lang="en">
<head>
<meta charset="utf-8">
<title>Mara Cole – Virtual Assistant Portfolio</title>
<link href="https://fonts.googleapis.com/css2?family=Jost:wght@400;500;600;700&family=Montserrat:wght@500;600&display=swap" rel="stylesheet">
<style>
  :root {
    --stage: #4d4d4d;
    --paper: #ffffff;
    --navy: #2f387a;
    --lavender: #7a86c6;
    --ink: #1c1c22;
    --photo-warm: #c9a25a;
    --photo-cool: #7f97b8;
  }
  * { box-sizing: border-box; margin: 0; padding: 0; }
  html, body {
    width: 1068px; height: 1200px; overflow: hidden;
    background: var(--stage);
  }
  .canvas { position: relative; width: 1068px; height: 1200px; }
  .page {
    position: absolute; width: 335px; height: 474px;
    background: var(--paper); overflow: hidden;
    font-family: "Jost", sans-serif; color: var(--ink);
  }
  .page--cover { left: 552px; top: 109px; }
  .page--about { left: 181px; top: 617px; }
  .page--services { left: 552px; top: 617px; }

  /* Cover */
  .brand-dot {
    position: absolute; left: 151px; top: 28px;
    width: 38px; height: 38px; border-radius: 50%;
    background: var(--lavender);
  }
  .brand-name {
    position: absolute; left: 0; width: 100%; top: 79px;
    text-align: center; font-family: "Montserrat", sans-serif;
    font-weight: 600; color: var(--navy);
    font-size: 22px; letter-spacing: 3.9px; line-height: 1;
    padding-left: 3.9px;
  }
  .brand-role {
    position: absolute; left: 0; width: 100%; top: 105px;
    text-align: center; font-family: "Montserrat", sans-serif;
    font-weight: 500; color: var(--navy);
    font-size: 13px; letter-spacing: 2.2px; line-height: 1;
    padding-left: 2.2px;
  }
  .cover-photo {
    position: absolute; left: 39px; top: 141px;
    width: 272px; height: 293px;
    background: linear-gradient(115deg, #3a2516 0%, var(--photo-warm) 38%, #e7dcc4 52%, var(--photo-cool) 78%, #4c5f80 100%);
  }

  /* Inner pages */
  .section { position: absolute; left: 23px; width: 288px; }
  .section-head { position: relative; height: 14px; }
  .section-mark {
    position: absolute; left: 1px; top: 0;
    width: 12px; height: 12px; border-radius: 50%;
    background: var(--lavender);
  }
  .section-title {
    position: absolute; left: 42px; top: 1px;
    font-weight: 700; font-size: 8px; color: var(--navy);
    letter-spacing: 0.2px; line-height: 1;
  }
  .section-rule {
    position: absolute; left: 19px; right: 0; top: 10px;
    border-top: 0.8px solid var(--navy);
  }
  .section-body {
    margin-left: 42px; margin-top: 2px;
    font-size: 7.3px; line-height: 8.1px;
  }
  .section-body p + p { margin-top: 6.4px; }

  .about { top: 50px; }
  .portrait {
    float: left; width: 80px; height: 76px;
    margin-left: -24px; margin-top: 4px; margin-right: 2px;
    shape-outside: circle(50%);
    position: relative;
  }
  .portrait-image {
    position: absolute; left: 2px; top: 0;
    width: 73px; height: 73px; border-radius: 50%;
    background: radial-gradient(circle at 45% 40%, #c9a889 0%, #8a6a52 45%, #5d7292 100%);
  }
  .about .section-body p:first-of-type { padding-left: 6px; }

  .credentials { top: 245px; }
  .why { top: 300px; }

  .footer {
    position: absolute; left: 0; top: 440px; width: 100%; height: 24px;
    background: var(--navy); color: #fff;
    font-size: 6.6px; display: flex; align-items: center;
    padding: 0 23px; justify-content: space-between;
  }
  .footer-sep { opacity: 0.9; }

  /* Services */
  .services { top: 50px; }
  .service-columns { display: flex; margin-left: 42px; margin-top: 2px; }
  .service-col { font-size: 6.85px; line-height: 8.05px; }
  .service-col--left { width: 131px; }
  .service-col--right { width: 120px; }
  .service-group + .service-group { margin-top: 8px; }
  .service-group h3 { font-weight: 600; font-size: 7px; color: var(--ink); }
  .service-group ul { list-style: none; }
  .service-group li { position: relative; padding-left: 8px; }
  .service-group li::before {
    content: ""; position: absolute; left: 1px; top: 3.3px;
    width: 2px; height: 2px; border-radius: 50%; background: var(--ink);
  }
</style>
</head>
<body>
<div class="canvas">

  <section class="page page--cover">
    <div class="brand-dot"></div>
    <h1 class="brand-name">MARA COLE</h1>
    <div class="brand-role">VIRTUAL ASSISTANT</div>
    <div class="cover-photo" role="img" aria-label="Photo collage: a judge's gavel on a warm-lit desk beside a woman on the phone working at a laptop"></div>
  </section>

  <section class="page page--about">
    <div class="section about">
      <div class="section-head"><span class="section-mark"></span><h2 class="section-title">ABOUT ME</h2><span class="section-rule"></span></div>
      <div class="section-body">
        <div class="portrait"><div class="portrait-image" role="img" aria-label="Portrait photo of the virtual assistant"></div></div>
        <p>Hello, I'm Mara Cole, a mother, coffee lover, and a passion for travel. I enjoy organisation and making life easy. With over 15 years of experience in the legal field, I have gained valuable experience whilst at the same time, perfecting my skills.</p>
        <p>Throughout my journey in the legal profession, I have held various roles, each contributing to my growth and expertise. Starting as a Rounds Clerk, I quickly advanced to the role of Administrative Assistant in the area of Litigation which involved leading a team of administration assistants focused on supporting legal professionals and litigation processes. This role was invaluable in that it taught me the importance of organisation, time management, attention to detail and multitasking.</p>
        <p>I then transitioned into Debt Recovery, where I thrived as a Paralegal. In this role, I took on the responsibility of managing my own caseload and providing comprehensive legal support independently. Attention to detail, meticulous research and effective communication became second nature. This allowed me to achieve successful resolutions while maintaining the utmost organization and professionalism.</p>
      </div>
    </div>

    <div class="section credentials">
      <div class="section-head"><span class="section-mark"></span><h2 class="section-title">CREDENTIALS</h2><span class="section-rule"></span></div>
      <div class="section-body">
        Certificate IV in Business (Legal Services)<br>
        Certificate III of Business Administration<br>
        Certificate II in Business
      </div>
    </div>

    <div class="section why">
      <div class="section-head"><span class="section-mark"></span><h2 class="section-title">WHY HIRE ME?</h2><span class="section-rule"></span></div>
      <div class="section-body">
        <p>A virtual assistant is an affordable alternative to hiring on-site administration support. Hire me for a once-off task or on a regular basis. I'm here to help you so get more time back in your day so you can focus on more important tasks. I want to save you time, as who has enough of that these days!</p>
        <p>I am known for my reliability, determination, ability to work diligently in fast-paced environments as well as delivering results. I take pride in my meticulous approach to the tasks I undertake. I adapt well to new technology.</p>
        <p>I am excited to embrace new opportunities that allow me to showcase my skill set expertise, provide dedicated support to professionals and that may involve my legal expertise. I am committed to making a positive impact wherever I go, bringing efficiency and structure.</p>
      </div>
    </div>

    <footer class="footer">
      <span>mara@mcva-office.com.au</span><span class="footer-sep">|</span>
      <span>0400 555 017</span><span class="footer-sep">|</span>
      <span>ABN: 12 345 678 901</span>
    </footer>
  </section>

  <section class="page page--services">
    <div class="section services">
      <div class="section-head"><span class="section-mark"></span><h2 class="section-title">WHAT CAN I DO FOR YOU?</h2><span class="section-rule"></span></div>
      <div class="service-columns">
        <div class="service-col service-col--left">
          <div class="service-group">
            <h3>General administration support</h3>
            <ul>
              <li>Document preparation including editing and formatting</li>
              <li>Spreadsheets</li>
              <li>Client correspondence</li>
              <li>Customer service / telephone calls</li>
              <li>Invoicing</li>
              <li>Bulk mail outs</li>
              <li>Data entry</li>
              <li>Database and records management</li>
            </ul>
          </div>
          <div class="service-group">
            <h3>Email management</h3>
            <ul>
              <li>Categorize and prepare sub folders</li>
              <li>Prioritize emails</li>
              <li>Send email correspondence</li>
            </ul>
          </div>
          <div class="service-group">
            <h3>Calendar &amp; diary management</h3>
            <ul>
              <li>Assist with scheduling appointments and meetings</li>
              <li>Scheduling reminders</li>
            </ul>
          </div>
          <div class="service-group">
            <h3>Travel arrangements</h3>
            <ul>
              <li>Assist with booking<br>intrastate/interstate travel</li>
              <li>Assist with car hire and<br>accommodation</li>
            </ul>
          </div>
        </div>
        <div class="service-col service-col--right">
          <div class="service-group">
            <h3>Software</h3>
            <ul>
              <li>Workspace Suite</li>
              <li>Brieflow Practice</li>
              <li>Matterbase</li>
            </ul>
          </div>
          <div class="service-group">
            <h3>Debt Collection</h3>
            <ul>
              <li>Assist with sending out overdue statements</li>
              <li>Issue demand letters</li>
              <li>Issue Claims and enforcement action in the Magistrates Court of Southland</li>
              <li>Negotiating payment arrangements</li>
              <li>Knowledge with Filewell portal</li>
            </ul>
          </div>
          <div class="service-group">
            <h3>Other</h3>
            <ul>
              <li>Online research</li>
              <li>Event coordination</li>
            </ul>
          </div>
          <div class="service-group">
            <h3>Legal</h3>
            <ul>
              <li>Filewell portal</li>
              <li>Preparing Court documents</li>
              <li>Filing Court Documents</li>
            </ul>
          </div>
        </div>
      </div>
    </div>

    <footer class="footer">
      <span>mara@mcva-office.com.au</span><span class="footer-sep">|</span>
      <span>0400 555 017</span><span class="footer-sep">|</span>
      <span>ABN: 12 345 678 901</span>
    </footer>
  </section>

</div>
</body>
</html>
```